snugSEAL - packaging design for plastic zip-lock mechansim

Looking for packaging designs for my patented product, which provides the ability to lock and close existing plastic bags, which have been opened up (like sugar or flour bag, snack bag, etc.). With applying snugSEAL to any bag once opened, the products can be held safe, locked and dry.
Please check my supporting documentation attached, including logos and packaging description.
The packaging design has to make clear to the customer:
- WHAT is this product for
- how to USA
- what are the BENEFITS and the VALUE
I am looking for a long term cooperation with the winning designer, as I will need multiple variations of the packaging depending on individual product usage. I am thinking of approximately 10 different variations in the future.
Updates
Project Deadline Extended Reason: Extending deadline to receive more designs. Please submit your designs according to my description. Let me know if any questions!This will be a long term cooperation as I will need subsequent designs for alternative product variations in the future. Added Saturday, October 22, 2016
Target Market(s)
All consumers who buy products in the supermarket. In particular when they buy products in bags (like salt, sugar, flour, detergents, snacks, ...)
Industry/Entity Type
Retail
Look and feel
Each slider illustrates characteristics of the customer's brand and the style your logo design should communicate.

```html
<!DOCTYPE html>
<html lang="en">
<head>
<meta charset="utf-8">
<title>snugSEAL – How you close after opening</title>
<link rel="stylesheet" href="https://fonts.googleapis.com/css2?family=Archivo+Black&family=Lato:wght@300;700;900&display=swap">
<style>
  :root {
    --backdrop: #f3c20c;
    --pack-red: #ec1c24;
    --ink: #0b0b0b;
    --paper: #ffffff;
    --label-yellow: #fff200;
    --bullet-red: #e4161e;
    --placeholder: #f1f1f1;
  }
  * { margin: 0; padding: 0; box-sizing: border-box; }
  html, body {
    width: 1200px;
    height: 1200px;
    overflow: hidden;
    background: var(--backdrop);
  }
  .canvas {
    position: relative;
    width: 1200px;
    height: 1200px;
  }
  .pack-front {
    position: absolute;
    left: 270px;
    top: 110px;
    width: 660px;
    height: 980px;
    background: var(--pack-red);
    overflow: hidden;
  }
  .headline {
    position: absolute;
    left: 0;
    right: 0;
    top: 105px;
    text-align: center;
    color: var(--ink);
  }
  .headline-main {
    display: block;
    font-family: "Archivo Black", sans-serif;
    font-size: 112px;
    line-height: 0.9;
    letter-spacing: -3px;
  }
  .headline-sub {
    display: block;
    font-family: "Lato", sans-serif;
    font-weight: 700;
    font-size: 58px;
    line-height: 0.95;
    letter-spacing: -2px;
  }
  .headline-sub.small {
    font-size: 46px;
  }
  .reveal-band {
    position: absolute;
    left: 0;
    right: 0;
    top: 372px;
    height: 240px;
    background: var(--ink);
    border-top: 10px solid var(--paper);
    border-bottom: 12px solid var(--paper);
  }
  .brand-name {
    position: absolute;
    left: 0;
    right: 0;
    top: 82px;
    text-align: center;
    font-family: "Lato", sans-serif;
    font-weight: 300;
    font-size: 68px;
    line-height: 1;
    color: var(--paper);
  }
  .usage-illustration {
    position: absolute;
    left: 150px;
    top: 630px;
    width: 240px;
    height: 300px;
    background: var(--placeholder);
  }
  .benefit-label {
    position: absolute;
    left: 280px;
    top: 770px;
    width: 238px;
    padding: 10px 12px 10px 14px;
    background: var(--label-yellow);
    transform: rotate(-12deg);
    transform-origin: left top;
    box-shadow: -8px 10px 14px rgba(0,0,0,0.18);
  }
  .benefit-list {
    list-style: none;
    font-family: "Archivo Black", sans-serif;
    font-size: 15px;
    line-height: 1.12;
    color: var(--ink);
    text-transform: uppercase;
  }
  .benefit-list li {
    position: relative;
    padding-left: 18px;
  }
  .benefit-list li.bullet::before {
    content: "";
    position: absolute;
    left: 0;
    top: 4px;
    width: 10px;
    height: 10px;
    border-radius: 50%;
    background: var(--bullet-red);
  }
</style>
</head>
<body>
  <main class="canvas">
    <section class="pack-front">
      <h1 class="headline">
        <span class="headline-main">HOW</span>
        <span class="headline-sub">you close</span>
        <span class="headline-sub small">after opening</span>
      </h1>

      <div class="reveal-band">
        <p class="brand-name">snugSEAL</p>
      </div>

      <div class="usage-illustration" role="img" aria-label="Illustration of a white bag with the seal strip clipped across its top, a dashed yellow circle highlighting the slider"></div>

      <div class="benefit-label">
        <ul class="benefit-list">
          <li class="bullet">Easy to attach</li>
          <li class="bullet">Fully to recycle</li>
          <li class="bullet">Works for paper</li>
          <li>and plastic bags</li>
          <li>in the same way</li>
        </ul>
      </div>
    </section>
  </main>
</body>
</html>
```